I need a logo design and a business card design for a new strategy consultancy that I set up called Corvanel LLC. We help clients make strategically important decisions, cutting through the cloud of noise. The design should imply clarity, simplicity and wisdom.

```html
<!DOCTYPE html>
<html lang="en">
<head>
<meta charset="utf-8">
<title>Corvanel LLC — Business Card</title>
<link rel="stylesheet" href="https://fonts.googleapis.com/css2?family=Work+Sans:wght@400;500;600&display=swap">
<style>
  :root {
    --brand-blue: #29a8e0;
    --ink: #3a3b3f;
    --rule: #55575c;
    --paper: #ffffff;
    --backdrop: #d9d9d9;
  }
  * { box-sizing: border-box; margin: 0; padding: 0; }
  html, body {
    width: 1200px; height: 930px; overflow: hidden;
    background: var(--backdrop);
    font-family: "Work Sans", sans-serif;
  }
  .stage {
    width: 1200px; height: 930px;
    display: flex; flex-direction: column;
    align-items: center; justify-content: center; gap: 56px;
  }
  .card {
    width: 600px; height: 343px;
    border-radius: 22px;
    position: relative; overflow: hidden;
    box-shadow: 0 6px 18px rgba(0,0,0,0.18);
  }
  /* front */
  .card-front { background: var(--brand-blue); }
  .world-map-area {
    position: absolute; left: 70px; top: 50px; width: 460px; height: 240px;
    background: radial-gradient(ellipse at center, rgba(255,255,255,0.16), rgba(255,255,255,0) 70%);
  }
  .front-wordmark {
    position: absolute; inset: 0;
    display: flex; align-items: center; justify-content: center;
    color: var(--paper);
    font-weight: 600; font-size: 44px; letter-spacing: 3px;
    white-space: nowrap;
  }
  /* back */
  .card-back { background: var(--paper); }
  .back-wordmark {
    position: absolute; left: 44px; top: 168px;
    display: flex; align-items: center; gap: 8px;
    color: var(--ink);
    font-weight: 600; font-size: 23px; letter-spacing: 1px;
    white-space: nowrap;
  }
  .wordmark-square { width: 11px; height: 11px; background: var(--brand-blue); flex: none; }
  .divider {
    position: absolute; left: 318px; top: 80px;
    width: 1.5px; height: 180px; background: var(--rule);
  }
  .contact-block { position: absolute; left: 342px; top: 82px; color: var(--ink); white-space: nowrap; }
  .person-name {
    color: var(--brand-blue); font-weight: 500; font-size: 19px; letter-spacing: 0.5px;
  }
  .person-role { font-size: 13px; margin-top: 2px; }
  .address { font-size: 13px; line-height: 1.45; margin-top: 14px; }
  .contact-list { list-style: none; margin-top: 14px; font-size: 13px; line-height: 1.6; }
  .contact-list li { display: flex; align-items: center; gap: 8px; }
  .contact-list svg { width: 11px; height: 11px; flex: none; }
  .accent { color: var(--brand-blue); }
</style>
</head>
<body>
<main class="stage">
  <section class="card card-front" aria-label="Card front">
    <div class="world-map-area" role="img" aria-label="Faint dotted world map pattern"></div>
    <div class="front-wordmark">CORVANEL LLC</div>
  </section>

  <section class="card card-back" aria-label="Card back">
    <div class="back-wordmark"><span class="wordmark-square"></span>CORVANEL LLC</div>
    <div class="divider"></div>
    <div class="contact-block">
      <p class="person-name">DANIEL HARROW</p>
      <p class="person-role">Director</p>
      <p class="address">418 Linden Avenue<br>Bayside, FL 32590</p>
      <ul class="contact-list">
        <li>
          <svg viewBox="0 0 12 12" aria-hidden="true"><path d="M2.5 1l2 2.2-1 1.3c.7 1.5 1.8 2.6 3.3 3.3l1.3-1 2.2 2-1.2 1.6C5.5 10.2 1.8 6.5 1 2.2z" fill="var(--brand-blue)"/></svg>
          555-204-3178
        </li>
        <li>
          <svg viewBox="0 0 12 12" aria-hidden="true"><rect x="1" y="2.5" width="10" height="7" rx="1" fill="none" stroke="var(--brand-blue)" stroke-width="1.2"/><path d="M1.5 3l4.5 3.5L10.5 3" fill="none" stroke="var(--brand-blue)" stroke-width="1.2"/></svg>
          info@corvanelllc.com
        </li>
        <li>
          <svg viewBox="0 0 12 12" aria-hidden="true"><circle cx="6" cy="6" r="4.8" fill="none" stroke="var(--brand-blue)" stroke-width="1.1"/><ellipse cx="6" cy="6" rx="2" ry="4.8" fill="none" stroke="var(--brand-blue)" stroke-width="1"/><path d="M1.2 6h9.6" stroke="var(--brand-blue)" stroke-width="1"/></svg>
          <span>www.<span class="accent">corvanelllc</span>.com</span>
        </li>
      </ul>
    </div>
  </section>
</main>
</body>
</html>
```